Horseriders ecommerce

I need the design of a web site and ecommerce for horse riders product. the actual site is brinamarket.it and is completely to rebuild.
the most important thing that must come out from the design is that this shop sells products for both type of riding: english and western and as well has products available and good for both. (accessories and horse care)
the site owners loves much more the western riding and they want to gain a good part of customers of it, that's why i ask you to give the central area and importance to the western products.
at http://www.keltorange.com you can see a site style that we like, especially for the inner pages of products.
colors and graphics elements must be related to the world of horse riding, but we want the design to keep elegance and style, without being so western!
you need to find a way to create a cool design, user friendly to buy and that gives the real impression of professionality and care.
please check this site: http://www.pemblyworks.it/
the style is not so nice in my opinion, but somehow the navigation is friendly
in attachment to the project I add the mockup of the home page. Abou the inner page, please feel free to create the correct layout and check the one of www.keltorange.com which I like especially for the product sheet.

p.s. you can change the color of the logo
Updates

Hello dear designers,
i've pushed a little the deadline.
I will give you feedback in a while.
thaks to all
Ginevra

Target Market(s)

horse riders
western riders
english riders
stables owners

Industry/Entity Type

Product

Requirements
Must have
• style, elegance and western atmosphere. GOOD SPACES to show products.
• MUST HAVE a base way to manage banners in home page
Nice to have
• images of horses, but the most important images are products
Should not have
• too many western elements

```html
<!DOCTYPE html>
<html lang="it">
<head>
<meta charset="utf-8">
<title>Sella Nord – Horse riding shop</title>
<link rel="stylesheet" href="https://fonts.googleapis.com/css2?family=Roboto:wght@300;400;500;700&family=Oswald:wght@400;500;600&display=swap">
<style>
:root{
  --red:#d3262b;
  --ink:#2b2b2b;
  --text:#555;
  --muted:#8a8a8a;
  --line:#e3e3e3;
  --panel:#f4f4f4;
  --dark:#3c3c3c;
  --white:#fff;
}
*{box-sizing:border-box;margin:0;padding:0}
html,body{width:1200px;height:3316px;overflow:hidden}
body{position:relative;font-family:"Roboto",Arial,sans-serif;color:var(--text);font-size:14px;background:#dfe6ec}
.backdrop{position:absolute;inset:0;background:linear-gradient(180deg,#c9d8e6 0%,#e8edf0 20%,#9fb0a0 45%,#b9c6b4 70%,#dfe4dc 100%)}
.site{position:absolute;left:72px;top:0;width:1056px;height:3316px;background:var(--white)}
.inner{width:1000px;margin:0 auto}
a{color:inherit;text-decoration:none}

.topbar{height:32px;border-bottom:1px solid var(--line);display:flex;align-items:center;justify-content:space-between;padding:0 28px;font-size:10px;color:var(--muted);letter-spacing:.3px;text-transform:uppercase}
.topbar nav{display:flex;gap:18px}

.header{height:136px;position:relative;display:flex;align-items:center;justify-content:center}
.social{position:absolute;left:28px;top:57px;display:flex;gap:8px}
.social span{width:22px;height:22px;border-radius:50%;background:var(--dark)}
.brand{display:flex;align-items:center;gap:12px}
.brand-dot{width:46px;height:46px;border-radius:50%;background:var(--red)}
.brand-name{font-size:34px;font-weight:700;color:var(--ink);letter-spacing:.5px;white-space:nowrap}
.cart-box{position:absolute;right:28px;top:44px;width:90px;font-size:10px;color:var(--muted);text-transform:uppercase;line-height:1.5;border-left:3px solid var(--red);padding-left:8px}
.cart-box strong{display:block;color:var(--red);font-size:13px}

.mainnav{height:52px;border-top:1px solid var(--line);border-bottom:1px solid var(--line);margin:0 28px;display:flex;align-items:center;gap:34px;padding-left:14px;font-size:12px;font-weight:500;color:var(--ink);text-transform:uppercase;letter-spacing:.4px}
.mainnav a.current{color:var(--red)}
.mainnav span{color:var(--line)}

.hero{margin:52px auto 0;height:440px;position:relative;background:linear-gradient(120deg,#6d8a5c 0%,#a7b48a 30%,#8a5a36 55%,#5a3620 80%,#3b2415 100%)}
.arrow{position:absolute;top:200px;width:26px;height:40px;background:rgba(60,60,60,.75);display:flex;align-items:center;justify-content:center}
.arrow.left{left:0}.arrow.right{right:0}

.promos{margin:28px auto 0;height:112px;display:flex;gap:40px}
.promo{flex:1;background:var(--dark);color:var(--white);display:flex;flex-direction:column;align-items:center;justify-content:center;border-bottom:4px solid var(--red)}
.promo h2{font-family:"Oswald",Arial,sans-serif;font-weight:500;font-size:44px;letter-spacing:2px;line-height:1;white-space:nowrap}
.promo p{font-size:11px;letter-spacing:1px;text-transform:uppercase;color:#ccc;margin-top:6px}

.section-title{display:flex;align-items:center;gap:20px;font-size:20px;font-weight:500;color:var(--ink);text-transform:uppercase;letter-spacing:1px}
.section-title::before,.section-title::after{content:"";flex:1;height:1px;background:var(--line)}

.categories{height:588px;padding-top:48px}
.cat-grid{display:flex;gap:40px;margin-top:20px}
.cat{width:306px}
.cat .photo{height:312px}
.cat h3{font-size:17px;font-weight:700;color:var(--ink);margin:22px 0 8px}
.cat p{font-size:12px;line-height:1.55;color:var(--text)}
.cat a{display:block;margin-top:10px;font-size:12px;color:var(--red)}
.ph-a{background:linear-gradient(150deg,#a56b3d,#6e3f22 60%,#3d2314)}
.ph-b{background:linear-gradient(150deg,#c89a6a,#8e2b24 55%,#3a1d12)}
.ph-c{background:linear-gradient(150deg,#50606e,#2d3b48 55%,#6a7a54)}

.tabs{height:36px;border-bottom:1px solid var(--line);display:flex;align-items:flex-end;gap:26px;font-size:14px;font-weight:500;text-transform:uppercase;color:var(--ink);position:relative}
.tabs a{padding-bottom:10px}
.tabs a.on{border-bottom:3px solid var(--red)}
.tab-arrows{position:absolute;right:0;bottom:10px;display:flex;gap:6px}
.tab-arrows span{width:18px;height:18px;border:1px solid var(--line);display:flex;align-items:center;justify-content:center}

.products{height:860px;padding-top:48px}
.prod-grid{display:grid;grid-template-columns:repeat(4,232px);column-gap:24px;row-gap:16px;margin-top:12px}
.prod{height:360px;text-align:center}
.prod .photo{height:232px;background:linear-gradient(160deg,#b07a4a,#6b3a1f 55%,#2f1a0e)}
.prod h4{font-size:14px;font-weight:400;color:var(--ink);margin-top:14px}
.price{font-size:15px;color:var(--red);margin-top:6px}
.price del{color:var(--muted);margin-right:4px}
.btn{display:block;margin:16px auto 0;height:32px;line-height:30px;border:1px solid #bbb;font-size:12px;font-weight:500;color:var(--ink);text-transform:uppercase}

.blog{height:412px;padding-top:44px}
.blog-grid{display:flex;gap:24px;margin-top:16px}
.post{flex:1}
.post .photo{height:152px}
.ph-gift{background:linear-gradient(135deg,#fbeaea,#f3c9c9)}
.ph-config{background:#a9a9a9;color:#fff;display:flex;align-items:center;justify-content:center;font-size:20px}
.ph-post{background:linear-gradient(135deg,#d9d2c2,#8a6242 55%,#4a2e1a)}
.post h3{font-size:16px;font-weight:500;color:var(--ink);margin-top:14px}
.meta{font-size:10px;color:var(--muted);text-transform:uppercase;margin:4px 0 8px}
.meta b{color:var(--red);font-weight:400}
.post p{font-size:12px;line-height:1.5}

.quote{height:200px;border-top:1px solid var(--line);border-bottom:1px solid var(--line);margin:0 28px;display:flex;flex-direction:column;align-items:center;justify-content:center}
.quote blockquote{font-size:32px;font-weight:300;color:var(--ink)}
.quote cite{font-style:normal;font-size:14px;color:var(--red);margin-top:8px}

.footer{height:328px;background:var(--panel);padding:44px 28px 0;display:flex;gap:36px}
.fcol{flex:1;font-size:12px;line-height:1.55}
.fcol h5{font-size:14px;font-weight:500;color:var(--ink);text-transform:uppercase;margin-bottom:16px}
.fbrand{display:flex;align-items:center;gap:8px;margin-bottom:14px}
.fbrand i{width:26px;height:26px;border-radius:50%;background:var(--red)}
.fbrand b{font-size:18px;color:var(--ink)}
.tags{display:flex;flex-wrap:wrap;gap:5px}
.tags span{background:var(--red);color:#fff;font-size:9px;padding:3px 7px;text-transform:uppercase}
.recent{display:flex;gap:10px;margin-bottom:14px}
.recent .thumb{width:56px;height:56px;background:#d8d8d8;flex:none}
.recent .price{font-size:12px;margin-top:2px}

.bottom{height:76px;display:flex;align-items:center;justify-content:space-between;padding:0 28px;font-size:11px;color:var(--muted)}
.cards{display:flex;gap:6px}
.cards span{width:38px;height:24px;border-radius:3px;background:#c9ccd2}
</style>
</head>
<body>
<div class="backdrop" role="img" aria-label="Background photo of mountains and a paddock fence under a blue sky"></div>

<div class="site">
  <div class="topbar">
    <span>Riding gear, saddles and horse care · free shipping over €99</span>
    <nav><a href="#">Wishlist</a><a href="#">My account</a><a href="#">Cart</a></nav>
  </div>

  <header class="header">
    <div class="social"><span></span><span></span><span></span><span></span></div>
    <a class="brand" href="#"><span class="brand-dot"></span><span class="brand-name">Sella Nord</span></a>
    <div class="cart-box">Item(s)<strong>£0</strong></div>
  </header>

  <nav class="mainnav">
    <a class="current" href="#">Home</a><span>|</span>
    <a href="#">Our products</a><span>|</span>
    <a href="#">How to buy</a><span>|</span>
    <a href="#">Who we are</a><span>|</span>
    <a href="#">Offers</a><span>|</span>
    <a href="#">Cart</a><span>|</span>
    <a href="#">Contact</a>
  </nav>

  <section class="hero inner" role="img" aria-label="Banner photo of a rider in a helmet beside her saddled horse">
    <span class="arrow left"><svg width="10" height="14"><path d="M8 1 2 7l6 6" stroke="#fff" stroke-width="2" fill="none"/></svg></span>
    <span class="arrow right"><svg width="10" height="14"><path d="m2 1 6 6-6 6" stroke="#fff" stroke-width="2" fill="none"/></svg></span>
  </section>

  <div class="promos inner">
    <div class="promo"><h2>FREE SHIPPING</h2><p>On all orders above €99</p></div>
    <div class="promo"><h2>THE BEST DEALS</h2><p>Save on every order, for better riding</p></div>
  </div>

  <section class="categories inner">
    <h2 class="section-title">Our product categories</h2>
    <div class="cat-grid">
      <article class="cat"><div class="photo ph-a" role="img" aria-label="Photo of an English saddle on a horse"></div>
        <h3>Monta inglese</h3><p>Lorem ipsum <b>dolor</b> sit amet, consectetur adipiscing elit, sed do eiusmod tempor incididunt ut labore.</p><a href="#">View the Category</a></article>
      <article class="cat"><div class="photo ph-b" role="img" aria-label="Photo of a western saddle"></div>
        <h3>Monta americana</h3><p>Lorem ipsum <b>dolor</b> sit amet, consectetur adipiscing elit, sed do eiusmod tempor incididunt ut labore.</p><a href="#">View the Category</a></article>
      <article class="cat"><div class="photo ph-c" role="img" aria-label="Photo of a horse wearing a stable rug"></div>
        <h3>Cura del cavallo</h3><p>Lorem ipsum <b>dolor</b> sit amet, consectetur adipiscing elit, sed do eiusmod tempor incididunt ut labore.</p><a href="#">View the Category</a></article>
    </div>
  </section>

  <section class="products inner">
    <div class="tabs"><a class="on" href="#">New arrivals</a><a href="#">Featured products</a>
      <div class="tab-arrows"><span><svg width="6" height="8"><path d="M5 1 1 4l4 3" stroke="#999" fill="none"/></svg></span><span><svg width="6" height="8"><path d="m1 1 4 3-4 3" stroke="#999" fill="none"/></svg></span></div></div>
    <div class="prod-grid">
      <div class="prod"><div class="photo" role="img" aria-label="Product photo of a saddle"></div><h4>Product 01</h4><div class="price"><del>£780.99</del>£599</div><a class="btn" href="#">Add to cart</a></div>
      <div class="prod"><div class="photo" role="img" aria-label="Product photo of a saddle"></div><h4>Product 02</h4><div class="price">From: £69.99</div><a class="btn" href="#">Select options</a></div>
      <div class="prod"><div class="photo" role="img" aria-label="Product photo of a saddle"></div><h4>Product 03</h4><div class="price">£489.99</div><a class="btn" href="#">Add to cart</a></div>
      <div class="prod"><div class="photo" role="img" aria-label="Product photo of a saddle"></div><h4>Product 04</h4><div class="price">£159.90</div><a class="btn" href="#">Add to cart</a></div>
      <div class="prod"><div class="photo" role="img" aria-label="Product photo of a saddle"></div><h4>Product 05</h4><div class="price">From: £53.59</div><a class="btn" href="#">Select options</a></div>
      <div class="prod"><div class="photo" role="img" aria-label="Product photo of a saddle"></div><h4>Product 06</h4><div class="price">From: £153.59</div><a class="btn" href="#">Select options</a></div>
      <div class="prod"><div class="photo" role="img" aria-label="Product photo of a saddle"></div><h4>Product 07</h4><div class="price">£889.99</div><a class="btn" href="#">Add to cart</a></div>
      <div class="prod"><div class="photo" role="img" aria-label="Product photo of a saddle"></div><h4>Product 08</h4><div class="price">£349.90</div><a class="btn" href="#">Add to cart</a></div>
    </div>
  </section>

  <section class="blog inner">
    <div class="tabs"><a class="on" href="#">Show all</a><a href="#">Blogroll</a><a href="#">Featured</a><a href="#">News</a>
      <div class="tab-arrows"><span><svg width="6" height="8"><path d="M5 1 1 4l4 3" stroke="#999" fill="none"/></svg></span><span><svg width="6" height="8"><path d="m1 1 4 3-4 3" stroke="#999" fill="none"/></svg></span></div></div>
    <div class="blog-grid">
      <article class="post"><div class="photo ph-gift" role="img" aria-label="Illustration of a gift card tied with a red ribbon"></div>
        <h3>Gift card</h3><div class="meta">March 02, 2013 by admin - <b>Leave the comment</b></div>
        <p>Lorem ipsum dolor sit amet, consectetur adipiscing elit, sed diam nonummy nibh euismod tincidunt ut laoreet dolore.</p></article>
      <article class="post"><div class="photo ph-config">Saddle Configurator</div>
        <h3>Saddle configurator</h3><div class="meta">January 2, 2013 by admin - <b>Leave the comment</b></div>
        <p>Lorem ipsum dolor sit amet, consectetur adipiscing elit, sed diam nonummy nibh euismod tincidunt ut laoreet dolore.</p></article>
      <article class="post"><div class="photo ph-post" role="img" aria-label="Photo of a rider on horseback"></div>
        <h3>Blog last post</h3><div class="meta">January 1, 2013 by admin - <b>Leave the comment</b></div>
        <p>Lorem ipsum dolor sit amet, consectetur adipiscing elit, sed diam nonummy nibh euismod tincidunt ut laoreet dolore.</p></article>
    </div>
  </section>

  <section class="quote">
    <blockquote>“qui possono andare le opinioni sui prodotti”</blockquote>
    <cite>- Happy Customer</cite>
  </section>

  <footer class="footer">
    <div class="fcol">
      <div class="fbrand"><i></i><b>Sella Nord</b></div>
      <p>Text of the printing and typesetting industry. Lorem Ipsum has been the industry's standard dummy text ever since the 1500s.</p>
    </div>
    <div class="fcol"><h5>Tag cloud</h5>
      <div class="tags"><span>Saddles</span><span>Bridles</span><span>Western</span><span>English</span><span>Boots</span><span>Rugs</span><span>Care</span><span>Helmets</span><span>Spurs</span><span>Pads</span><span>Gifts</span><span>Offers</span><span>Reins</span><span>Bits</span></div>
    </div>
    <div class="fcol"><h5>Get in touch</h5>
      <p>Text of the printing and typesetting industry. Lorem Ipsum has been the industry's standard dummy text ever since the 1500s.</p>
    </div>
    <div class="fcol"><h5>Recent product</h5>
      <div class="recent"><div class="thumb" role="img" aria-label="Product thumbnail"></div><div><p>Has been the industry's standard</p><div class="price">£399</div></div></div>
      <div class="recent"><div class="thumb" role="img" aria-label="Product thumbnail"></div><div><p>Has been the industry's standard</p><div class="price">£69.99</div></div></div>
    </div>
  </footer>

  <div class="bottom">
    <div class="cards"><span></span><span></span><span></span><span></span><span></span></div>
    <span>All Rights Reserved</span>
  </div>
</div>
</body>
</html>
```